Create new HOME PAGE from existing design

Please read carefully and follow instructions or your design will not be considered. Please ask if you have any questions or need more details.
I have an existing ebay store design that I would like to move off ebay and turn into an ecommerce website. The goal for this project is to take the existing design and create a new website HOME PAGE ONLY. After I have the home page design, I will most likely work with the designer to create the additional website pages for the store, but no additional pages are required for this contest, and no coding is requested as part of this project.
The design files for the existing ebay store design are included below. If you need anything else let me know. The instructions are to use the existing design theme and elements to create a new ecommerce website HOME PAGE. This will not be a straight 1 to 1 conversion, I am looking for a new design based off the existing theme. Graphic elements from the existing ebay store design can be used, or new graphic elements can be created to better fit the theme. This current ebay store design has a high degree of graphic detail, and this same level of detail should exist in the new website home page. The same background should be used and the color scheme should not be changed.
Page should be a maximum width of 1200px, and I would like the design to be responsive.
This website will be a mixed ecommerce site that promotes both products and services. The home page will not be entirely dedicated to ecommerce. A large portion of the top section, below the header, will be reserved for promotion boxes or information. I would like a scrolling bar with the manufacturer logos from the "products we sell" page somewhere near the top half of the page. The bottom half of the home page will be used to display a few items or categories. I am open to ideas so don't be afraid to be creative.
Here is an example:
http://www.tonevaultexample.com/
This is similar to what I'm looking for in that most of the page is dedicated to promotion boxes, with only 1 row of items displayed on the home page. Overall I think the page and promotion boxes are too big and I do not want my site to look like this.

```html
<!DOCTYPE html>
<html lang="en">
<head>
<meta charset="utf-8">
<title>Relay Gear Supply – Home</title>
<link rel="stylesheet" href="https://fonts.googleapis.com/css2?family=Poppins:wght@300;400;500;600;700&display=swap">
<style>
:root{
  --bg-top:#b7c1b8;
  --bg-mid:#a4afa6;
  --bg-bottom:#8f9a91;
  --panel:#d9e3d8;
  --panel-soft:rgba(222,231,221,.9);
  --frame:#eef2ed;
  --ink:#2f3331;
  --ink-soft:#5d645f;
  --dark:#3c3f3d;
  --btn:#7d877f;
  --line:#b2bdb3;
  --footer:#4a3b36;
  --footer-ink:#d9cfc9;
  --white:#ffffff;
}
*{box-sizing:border-box;margin:0;padding:0}
html,body{width:1200px;height:2660px;overflow:hidden}
body{font-family:"Poppins",sans-serif;color:var(--ink);position:relative;
  background:linear-gradient(160deg,var(--bg-top) 0%,var(--bg-mid) 45%,var(--bg-bottom) 100%)}
.streaks{position:absolute;left:0;top:0;width:1200px;height:2260px;pointer-events:none;z-index:0}
.topbar,.header,.wrap{position:relative;z-index:1}

.topbar{height:22px;background:var(--dark);display:flex;align-items:center;justify-content:space-between;padding:0 80px;font-size:10px;color:#e6e6e6}
.social{display:flex;gap:8px}
.social span{width:12px;height:12px;border-radius:50%;background:#cfd4d0;display:block}
.topnav{display:flex}
.topnav a{color:#fff;text-decoration:none;padding:0 14px;border-left:1px solid #666}
.topnav a:first-child{border-left:none}
.contact-mini{display:flex;gap:20px}

.header{height:108px;display:flex;align-items:center;padding:0 80px;justify-content:space-between}
.logo{display:flex;align-items:center;gap:10px;color:var(--white);font-weight:600;font-size:20px}
.logo i{width:44px;height:44px;border-radius:50%;background:var(--white);display:block;opacity:.9}
.search{display:flex;height:30px;width:420px;margin-left:60px}
.search .cat{width:110px;background:#eef1ee;border:1px solid #aab2ab;font-size:10px;display:flex;align-items:center;justify-content:space-between;padding:0 8px}
.search .field{flex:1;background:#fff;font-size:10px;color:#999;display:flex;align-items:center;padding:0 10px}
.search .go{width:34px;background:var(--dark)}
.cart{display:flex;align-items:center;gap:10px;font-size:10px;color:var(--ink)}
.cart i{width:34px;height:34px;border-radius:50%;background:#eef1ee;display:block}

.wrap{padding:0 80px}
.hero{height:448px;background:#f1f2ef;display:flex;overflow:hidden;border:3px solid var(--frame)}
.hero-text{padding:60px 0 0 40px;width:400px;flex:none}
.hero-text h1{font-size:44px;line-height:1.18;font-weight:600;color:var(--ink)}
.btn{display:inline-block;background:var(--btn);color:#fff;font-size:11px;padding:9px 26px;border-radius:20px;letter-spacing:.5px}
.hero-text .btn{margin-top:30px}
.hero-photo{flex:1;background:
  radial-gradient(ellipse 26% 34% at 52% 52%,#d8d8d3 0%,rgba(216,216,211,0) 100%),
  linear-gradient(180deg,#f4f4f1 0%,#ecebe7 62%,#d8cbb6 76%,#c6ae8c 100%)}

.promos{display:flex;gap:28px;margin-top:32px;height:200px}
.promo{flex:1;display:flex;background:var(--panel-soft);border:4px solid var(--frame)}
.promo-photo{width:56%}
.p1{background:linear-gradient(135deg,#e9e5da 0%,#e4c65a 45%,#b89a5a 70%,#9ea59d 100%)}
.p2{background:linear-gradient(160deg,#efece6 0%,#d8c7a6 45%,#a88a62 75%,#8f948d 100%)}
.p3{background:linear-gradient(145deg,#f1efe9 0%,#d7d2c4 40%,#e5bf52 70%,#a6a9a2 100%)}
.promo-text{flex:1;padding:30px 12px;font-size:26px;font-weight:600;line-height:1}
.promo-text small{display:block;font-size:11px;font-weight:500;margin:6px 0 14px;color:var(--ink-soft);text-transform:uppercase}
.promo-text .btn{font-size:9px;padding:5px 14px;border-radius:3px;background:transparent;color:var(--ink);border:1px solid var(--ink)}

.welcome{margin-top:40px;height:440px;background:var(--panel-soft);text-align:center;padding:46px 70px}
.welcome-title{display:flex;align-items:center;justify-content:center;gap:30px;font-size:50px;font-weight:300}
.welcome-title::before,.welcome-title::after{content:"";width:240px;height:1px;background:#6f7a72}
.welcome h2{font-size:26px;font-weight:300;letter-spacing:2px;margin:8px 0 30px;color:#55605a}
.welcome p{font-size:12px;line-height:1.9;color:var(--ink-soft);text-align:left}
.welcome .btn{margin-top:40px;padding:11px 34px}

.shop{display:flex;gap:24px;margin-top:40px;height:696px}
.cats{width:328px;list-style:none;background:var(--panel)}
.cats li{height:53.5px;border-bottom:1px solid var(--line);display:flex;align-items:center;padding-left:16px;font-size:14px}
.cats li:last-child{border-bottom:none}
.grid{flex:1;display:grid;grid-template-columns:1fr 1fr;gap:32px 28px}
.card{background:linear-gradient(180deg,#c6ccc6,#aeb6af);text-align:center;padding:18px;font-size:12px}
.card .thumb{height:170px;margin:0 50px 18px;border-radius:4px}
.t1{background:linear-gradient(135deg,#2c2f32,#4a5a6a 60%,#565b60)}
.t2{background:linear-gradient(135deg,#2b2b2b,#4a4a48)}
.t3{background:radial-gradient(circle,#f4f4f2 40%,rgba(200,204,199,0) 70%)}
.t4{background:linear-gradient(180deg,#3a3a3a,#707070)}
.price{margin:10px 0 6px;display:flex;justify-content:center;gap:14px;align-items:center}
.price s{color:#6a6f6b}
.stars{letter-spacing:2px;color:#444}
.buy{font-size:10px;margin-top:12px}

.brands{margin-top:40px;height:132px;background:var(--panel-soft);border:4px solid var(--frame);display:flex;align-items:center;justify-content:space-around;padding:0 30px}
.badge{height:40px;border-radius:4px}

.footer{position:absolute;left:0;right:0;top:2262px;bottom:0;background:var(--footer);color:var(--footer-ink);font-size:11px;z-index:1}
.footer-cols{display:flex;padding:56px 80px 0;gap:80px}
.footer-cols h4{font-size:11px;font-weight:500;letter-spacing:1px;margin-bottom:22px;color:#fff}
.col1{width:300px}.col2{width:330px}.col3{flex:1}
.line{display:flex;gap:14px;align-items:flex-start;margin-bottom:16px;line-height:1.6}
.line svg{flex:none;margin-top:2px}
.dots{display:flex;gap:10px;margin-top:6px}
.dots span{width:18px;height:18px;border-radius:50%;background:#e8dfda;display:block}
.links{display:grid;grid-template-columns:1fr 1fr;gap:8px;margin-top:8px}
.news{display:flex;height:32px;margin-bottom:34px}
.news .field{flex:1;background:#fff;color:#999;display:flex;align-items:center;padding:0 10px}
.news .go{width:50px;background:#7b7370;color:#fff;display:flex;align-items:center;justify-content:center;font-weight:600}
.cards{display:flex;gap:8px;margin-top:10px}
.cards span{width:42px;height:26px;border-radius:3px;display:block}
.copy{position:absolute;bottom:18px;left:0;right:0;text-align:center;font-size:10px;color:#b9aca5}
</style>
</head>
<body>
<svg class="streaks" viewBox="0 0 1200 2260" aria-hidden="true">
  <g stroke="#ffffff" fill="none">
    <line x1="1200" y1="120" x2="700" y2="700" stroke-width="2" stroke-opacity=".35"/>
    <line x1="1200" y1="300" x2="820" y2="760" stroke-width="1" stroke-opacity=".3"/>
    <line x1="0" y1="520" x2="420" y2="980" stroke-width="2" stroke-opacity=".25"/>
    <line x1="0" y1="1500" x2="300" y2="1200" stroke-width="1.5" stroke-opacity=".3"/>
    <line x1="1200" y1="1700" x2="900" y2="2100" stroke-width="1.5" stroke-opacity=".25"/>
    <line x1="60" y1="2240" x2="360" y2="1880" stroke-width="1" stroke-opacity=".25"/>
  </g>
  <polygon points="1200,40 1200,260 960,520" fill="#ffffff" fill-opacity=".08"/>
  <polygon points="0,1300 0,1700 220,1420" fill="#ffffff" fill-opacity=".07"/>
</svg>

<div class="topbar">
  <div class="social"><span></span><span></span><span></span><span></span><span></span></div>
  <nav class="topnav"><a href="#">Home</a><a href="#">About Us</a><a href="#">Contact Us</a></nav>
  <div class="contact-mini"><span>sales@relaygear.example</span><span>01632 960418</span></div>
</div>

<header class="header">
  <div class="logo"><i></i>Relay Gear Supply</div>
  <div class="search"><div class="cat">Categories <span>▾</span></div><div class="field">Search Here</div><div class="go"></div></div>
  <div class="cart"><span>Cart $0.00</span><i></i></div>
</header>

<main class="wrap">
  <section class="hero">
    <div class="hero-text">
      <h1>From Only<br>$389.00<br>ex.VAT</h1>
      <span class="btn">SHOP NOW</span>
    </div>
    <div class="hero-photo" role="img" aria-label="White lounge chair and wooden side table with a vase on a light wooden floor"></div>
  </section>

  <section class="promos">
    <div class="promo"><div class="promo-photo p1" role="img" aria-label="Office with yellow chairs around a table"></div><div class="promo-text">40%<small>on office items</small><span class="btn">Shop Now</span></div></div>
    <div class="promo"><div class="promo-photo p2" role="img" aria-label="Meeting room with a wooden table"></div><div class="promo-text">40%<small>on office items</small><span class="btn">Shop Now</span></div></div>
    <div class="promo"><div class="promo-photo p3" role="img" aria-label="Open plan office with desks and yellow seats"></div><div class="promo-text">40%<small>on office items</small><span class="btn">Shop Now</span></div></div>
  </section>

  <section class="welcome">
    <div class="welcome-title">Welcome</div>
    <h2>TO RELAY GEAR SUPPLY</h2>
    <p>Our team supplies control panels, keypads, processors, audio and video distribution, lighting and wireless parts for homes, offices and venues. Every item ships from stock, tested and ready to install, with friendly advice from people who design and fit these systems every day. Ask us about full project support, pre-configured bundles and trade pricing for installers across the country.</p>
    <span class="btn">Learn More</span>
  </section>

  <section class="shop">
    <ul class="cats">
      <li>Home</li><li>Touchpanels</li><li>Keypads</li><li>Controllers</li><li>Control Cards</li><li>Media Matrix</li><li>Quick Link</li><li>Audio Distribution</li><li>Video Distribution</li><li>Mesh Net</li><li>Lighting</li><li>Wireless Components</li><li>Accessories</li>
    </ul>
    <div class="grid">
      <article class="card"><div class="thumb t1" role="img" aria-label="Wall touch panel"></div><div>Vista Panel™ 3x</div><div class="price"><span><s>$38.99</s> | $32.99</span><span class="stars">★★★★☆</span></div><div class="buy">BUY NOW</div></article>
      <article class="card"><div class="thumb t2" role="img" aria-label="Rack control processor"></div><div>Vista Panel™ 3x</div><div class="price"><span><s>$38.99</s> | $32.99</span><span class="stars">★★★★☆</span></div><div class="buy">BUY NOW</div></article>
      <article class="card"><div class="thumb t3" role="img" aria-label="Ceiling occupancy sensor"></div><div>Vista Panel™ 3x</div><div class="price"><span><s>$38.99</s> | $32.99</span><span class="stars">★★★★☆</span></div><div class="buy">BUY NOW</div></article>
      <article class="card"><div class="thumb t4" role="img" aria-label="Audio amplifier unit"></div><div>Vista Panel™ 3x</div><div class="price"><span><s>$38.99</s> | $32.99</span><span class="stars">★★★★☆</span></div><div class="buy">BUY NOW</div></article>
    </div>
  </section>

  <section class="brands" aria-label="Manufacturers we sell">
    <div class="badge" style="width:130px;background:#4a4a48"></div>
    <div class="badge" style="width:46px;height:46px;border-radius:50%;background:#2d4a8a"></div>
    <div class="badge" style="width:120px;background:#b23a30"></div>
    <div class="badge" style="width:100px;background:#274a86"></div>
    <div class="badge" style="width:90px;background:#c8302a"></div>
    <div class="badge" style="width:110px;background:#3a6aa6"></div>
  </section>
</main>

<footer class="footer">
  <div class="footer-cols">
    <div class="col1">
      <h4>CONTACT INFORMATION</h4>
      <div class="line"><svg width="12" height="14" viewBox="0 0 12 14"><path d="M6 0a5 5 0 0 0-5 5c0 4 5 9 5 9s5-5 5-9a5 5 0 0 0-5-5zm0 7a2 2 0 1 1 0-4 2 2 0 0 1 0 4z" fill="#e8dfda"/></svg><span>22 Larkfield Road, Easton,<br>EA4 7QT, United Kingdom</span></div>
      <div class="line"><svg width="12" height="12" viewBox="0 0 12 12"><path d="M2 0l3 3-1.5 1.5a7 7 0 0 0 4 4L9 7l3 3-2 2C5 12 0 7 0 2z" fill="#e8dfda"/></svg><span>01632 960418</span></div>
      <div class="line"><svg width="14" height="10" viewBox="0 0 14 10"><rect width="14" height="10" rx="1" fill="#e8dfda"/><path d="M0 0l7 6 7-6" stroke="#4a3b36" fill="none"/></svg><span>sales@relaygear.example</span></div>
      <div class="dots"><span></span><span></span><span></span><span></span></div>
    </div>
    <div class="col2">
      <h4>BE THE FIRST TO KNOW</h4>
      <p style="line-height:1.7;margin-bottom:28px">Join our list for new stock, offers and install tips.</p>
      <h4>MY ACCOUNT</h4>
      <div class="links"><span>Home</span><span>Contact Us</span><span>About Us</span><span>Register</span></div>
    </div>
    <div class="col3">
      <h4>NEWSLETTER</h4>
      <div class="news"><div class="field">Your email</div><div class="go">GO</div></div>
      <h4>PAYMENT OPTIONS</h4>
      <div class="cards"><span style="background:#f0ece9"></span><span style="background:#2a5caa"></span><span style="background:#e0a030"></span><span style="background:#3b7bc8"></span></div>
    </div>
  </div>
  <div class="copy">Copyright © Relay Gear Supply. Terms and Conditions</div>
</footer>
</body>
</html>
```